Business card design needed

A laid back coffee shop that has a great feel, that becomes a bar and grill at night. We are also wanting to cater for functions etc.
The business itself is painted dark blue/charcoal and has red doors.
Would like a logo that will be recognised when seen.

Industry/Entity Type

Coffee Shop

Contact Information for Business Card

The Lantern Coffee Bar & Grill
14b Wattle Rd
Kelmora NSW 2318
Ph. 02 4817 3362

Logo Text

Logo styles of interest
Emblem Logo
Abstract Logo
Wordmark Logo
Requirements
Must have
• A loyalty card on the back with 2 rows of 7 stamp spaces and a place to write a name and phone number (for a draw)

```html
<!DOCTYPE html>
<html lang="en">
<head>
<meta charset="utf-8">
<title>The Lantern Coffee Bar &amp; Grill – Business Card</title>
<link rel="stylesheet" href="https://fonts.googleapis.com/css2?family=Nunito+Sans:wght@300;400;700;800&display=swap">
<style>
  :root {
    --backdrop: #4a565b;
    --brand-blue: #2369db;
    --deep-blue: #153f82;
    --card-white: #ffffff;
    --soft-grey: #b9b9b9;
    --ink: #111111;
    --rule: #555555;
    --stamp-ring: #333333;
    --stamp-fill: #f6f6f6;
  }
  * { margin: 0; padding: 0; box-sizing: border-box; }
  html, body {
    width: 1200px; height: 1000px; overflow: hidden;
    background: var(--backdrop);
    font-family: "Nunito Sans", Arial, sans-serif;
  }
  .canvas { position: relative; width: 1200px; height: 1000px; }

  .card { position: absolute; overflow: hidden; }
  .card-front {
    left: 215px; top: 40px; width: 778px; height: 432px;
    background: var(--brand-blue);
  }
  .card-back {
    left: 215px; top: 510px; width: 784px; height: 435px;
    background: var(--card-white);
  }

  .emblem-area {
    position: absolute; left: -40px; top: 0; width: 340px; height: 432px;
  }

  .wordmark { position: absolute; color: var(--card-white); font-weight: 700; line-height: 1; }
  .wordmark-the { left: 417px; top: 148px; font-size: 34px; }
  .wordmark-name { left: 347px; top: 160px; font-size: 94px; letter-spacing: -1px; }
  .wordmark-tagline { left: 418px; top: 262px; font-size: 36px; }

  .entry-row { position: absolute; left: 68px; top: 552px; width: 660px; height: 30px; }
  .entry-label { position: absolute; left: 0; top: 4px; color: var(--brand-blue); font-size: 18px; font-weight: 300; }
  .entry-line { position: absolute; top: 28px; height: 1px; background: var(--rule); }
  .entry-line.name { left: 62px; width: 247px; }
  .entry-line.phone { left: 345px; width: 312px; }
  .phone-icon { position: absolute; left: 316px; top: 12px; }

  .stamp-grid {
    position: absolute; left: 147px; top: 123px;
    display: grid; grid-template-columns: repeat(7, 72px);
    column-gap: 13.3px; row-gap: 14px;
  }
  .stamp {
    width: 72px; height: 72px; border-radius: 50%;
    border: 1px solid var(--stamp-ring);
    background: radial-gradient(circle at 50% 40%, #ffffff 0%, var(--stamp-fill) 70%, #e6e6e6 100%);
    box-shadow: 0 6px 5px -3px rgba(0,0,0,0.25);
  }

  .footer-name {
    position: absolute; right: 55px; top: 333px;
    color: var(--brand-blue); font-size: 24px; font-weight: 800;
  }
  .footer-address {
    position: absolute; left: 47px; top: 368px;
    color: var(--ink); font-size: 26px; font-weight: 400;
  }
</style>
</head>
<body>
<main class="canvas">

  <section class="card card-front" aria-label="Card front">
    <svg class="emblem-area" viewBox="0 0 340 432" role="img" aria-label="Large brand emblem area in deep blue">
      <defs>
        <radialGradient id="floor-shade" cx="50%" cy="50%" r="50%">
          <stop offset="0%" stop-color="#0f2f66" stop-opacity="0.7"/>
          <stop offset="100%" stop-color="#0f2f66" stop-opacity="0"/>
        </radialGradient>
      </defs>
      <ellipse cx="200" cy="385" rx="170" ry="32" fill="url(#floor-shade)"/>
      <circle cx="190" cy="215" r="150" fill="var(--deep-blue)"/>
    </svg>
    <div class="wordmark wordmark-the">The</div>
    <div class="wordmark wordmark-name">Lantern</div>
    <div class="wordmark wordmark-tagline">Coffee Bar &amp; Grill</div>
  </section>

  <section class="card card-back" aria-label="Card back – loyalty card">
    <div class="entry-row" style="top:42px">
      <span class="entry-label">Name:</span>
      <span class="entry-line name"></span>
      <svg class="phone-icon" width="22" height="16" viewBox="0 0 22 16" aria-label="Phone">
        <path d="M1 6 C1 1 21 1 21 6 L21 8 L16 8 L15 5 L7 5 L6 8 L1 8 Z" fill="var(--brand-blue)"/>
        <path d="M5 9 L17 9 L20 15 L2 15 Z" fill="var(--brand-blue)"/>
        <circle cx="11" cy="11.5" r="2" fill="#fff"/>
      </svg>
      <span class="entry-line phone"></span>
    </div>

    <div class="stamp-grid" aria-label="14 stamp spaces">
      <div class="stamp"></div><div class="stamp"></div><div class="stamp"></div><div class="stamp"></div>
      <div class="stamp"></div><div class="stamp"></div><div class="stamp"></div>
      <div class="stamp"></div><div class="stamp"></div><div class="stamp"></div><div class="stamp"></div>
      <div class="stamp"></div><div class="stamp"></div><div class="stamp"></div>
    </div>

    <div class="footer-name">The Lantern Coffee Bar &amp; Grill</div>
    <div class="footer-address">14b Wattle Rd, Kelmora NSW 2318, Ph. 02 4817 3362</div>
  </section>

</main>
</body>
</html>
```